Verpackungsdesign für Wellness- und Saunaprodukte
Zielgruppe
Brisavo ist ein junges Start-Up, das sich auf Wellness- und Saunaprodukte spezialisiert hat. Unsere Zielgruppe besteht zu beinahe gleichen Teilen aus männlichen und weiblichen Personen zwischen 30 und 60 Jahren. Unsere Produkte befinden sich eher im mittel- bis höherpreisigen Segment, daher streben wir ein hochwertiges Design für unsere Verpackungen an. Unsere Produktpalette reicht von Mentholkristallen, Saunaaufgüssen, bis hin zu Textilien für den Wellnessbereich und soll dementsprechend Menschen ansprechen, die sich einen gewissen Luxus im Alltag auch gönnen.
Aufgabenstellung
Inspiriert von der skandinavischen Sauna Kultur, möchten wir Momente der Erholung und
Entspannung in den Alltag unserer Kunden bringen. Die Geschichte des Saunierens ist eng mit der skandinavischen Kultur verbunden und skandinavische Stilelemente sind zeitgemäß und sprechen ein breites Publikum an. Das Design muss auf Dosen/Tiegel , Karton Verpackungen und Flaschen verschiedener Größen adaptierbar sein (siehe Bild im Anhang).
40g Tiegel(transparent) Höhe 40mm Durchmesser 60mm (ohne Deckel Silber gebürstet)
100g Tiegel(transparent) Höhe 53mm Durchmesser 71mm (ohne Deckel Silber gebürstet)
200g Tiegel(transparent) Höhe 65mm Durchmesser 90mm (ohne Deckel Silber gebürstet)
Karton Verpackung 124,5x49x49mm
Karton Verpackung 100x100x100mm
Flaschenetikett 134x67mm (Braunglas, schwarzer Deckel)
Es soll ein passendes Keyvisual erstellt werden.
Im Anhang sieht man die Verpackungen, Dosen, Flaschen sowie unsere ersten Design Entwürfe (an diese Anordnung der Elemente kann sich der Designer orientieren ). Das Logo bleibt wie gegeben. Das Produkt für die Tiegel soll Mentholkristalle sein.

```html
<!DOCTYPE html>
<html lang="de">
<head>
<meta charset="utf-8">
<title>Brisavo – Nordische Fichte Saunaaufguss Etikett</title>
<link rel="stylesheet" href="https://fonts.googleapis.com/css2?family=Libre+Baskerville:wght@400;700&display=swap">
<style>
  :root {
    --canvas-bg: #ececec;
    --label-bg: #f3f4f2;
    --label-pattern: #e4e6e3;
    --ink-grey: #8a8a8a;
    --ink-dark: #6f6f6f;
    --line-grey: #7c7c7c;
    --ornament-tone: #d9dad8;
    --emblem-teal: #1f8a7f;
    --emblem-teal-dark: #15675f;
  }
  * { margin: 0; padding: 0; box-sizing: border-box; }
  html, body {
    width: 1200px;
    height: 1200px;
    overflow: hidden;
    background: var(--canvas-bg);
  }
  .bottle-label {
    position: absolute;
    left: 250px;
    top: 169px;
    width: 700px;
    height: 862px;
    background: var(--label-bg);
    font-family: "Libre Baskerville", Georgia, serif;
  }
  .label-pattern {
    position: absolute;
    inset: 0;
    background:
      linear-gradient(90deg, var(--label-pattern) 0%, rgba(243,244,242,0) 16%, rgba(243,244,242,0) 84%, var(--label-pattern) 100%),
      radial-gradient(ellipse at 50% 30%, #eeefec 0%, var(--label-bg) 60%);
  }
  .brand {
    position: absolute;
    top: 120px;
    left: 0;
    width: 100%;
    text-align: center;
    font-size: 30px;
    font-weight: 400;
    color: var(--ink-grey);
    letter-spacing: 1px;
  }
  .product-name {
    position: absolute;
    top: 320px;
    left: 0;
    width: 100%;
    text-align: center;
    font-size: 40px;
    font-weight: 700;
    color: var(--ink-grey);
    letter-spacing: 0.5px;
  }
  .emblem {
    position: absolute;
    left: 260px;
    top: 433px;
    width: 180px;
    height: 180px;
    border-radius: 50%;
    background: radial-gradient(circle at 40% 35%, var(--emblem-teal), var(--emblem-teal-dark));
  }
  .category-box {
    position: absolute;
    left: 155px;
    top: 637px;
    width: 402px;
    height: 92px;
    border: 1.5px solid var(--line-grey);
    display: flex;
  }
  .category-box span {
    display: flex;
    align-items: center;
    justify-content: center;
    font-size: 29px;
    font-weight: 700;
    color: var(--ink-dark);
  }
  .category-box .category-left { flex: 0 0 178px; }
  .category-box .category-right {
    flex: 1;
    border-left: 1.5px solid var(--line-grey);
  }
  .wave-ornament {
    position: absolute;
    left: 155px;
    top: 747px;
    width: 402px;
    height: 38px;
    background: linear-gradient(180deg, var(--label-bg) 0%, var(--ornament-tone) 50%, var(--label-bg) 100%);
  }
</style>
</head>
<body>
  <div class="bottle-label">
    <div class="label-pattern" role="img" aria-label="Dezentes helles skandinavisches Schneeflockenmuster im Etiketthintergrund"></div>
    <div class="brand">Brisavo</div>
    <div class="product-name">Nordische Fichte</div>
    <div class="emblem" role="img" aria-label="Türkisfarbenes rundes Emblem mit skandinavischem Schneeflockenmuster"></div>
    <div class="category-box">
      <span class="category-left">SAUNA</span>
      <span class="category-right">AUFGUSS</span>
    </div>
    <div class="wave-ornament" role="img" aria-label="Zierornament aus zwei grauen Wellenlinien"></div>
  </div>
</body>
</html>
```